Riverpeak Analytics needs new design business card

We are video surveillance and analytics software development company.
I am looking for a professional business card.
Our website is www.riverpeakanalytics.example.au
Please have a loo and get the feel for who we are and what we do.
I do not know what else to give you apart from good luck and I hope your design gets selected.
Thank you very much for participating
Business
Contact Information for Business Card
Address
27/15 Marlowe Street Fernbrook NSW 2199
Telephone 1300 582 417
Mobile 0450 731 258
email: marcus@riverpeakanalytics.example.au
name
Marcus Helvard
Position
Managing Director
Font styles to use
Other font styles liked:
- Arial
Look and feel

```html
<!DOCTYPE html>
<html lang="en">
<head>
<meta charset="utf-8">
<title>Riverpeak Analytics – Business Card</title>
<link href="https://fonts.googleapis.com/css2?family=Arimo:wght@400;700&display=swap" rel="stylesheet">
<style>
  :root {
    --stage: #e7e3dc;
    --card-white: #ffffff;
    --card-grey-top: #a3a4a6;
    --card-grey-bottom: #8e8f91;
    --brand-blue: #1d4f8c;
    --name-blue: #2a6db5;
    --ink: #111111;
    --orange-light: #f6ad2e;
    --orange-deep: #e0860f;
    --edge-blue: #1f5aa6;
  }
  * { box-sizing: border-box; margin: 0; padding: 0; }
  html, body {
    width: 1200px; height: 1023px; overflow: hidden;
    background: var(--stage);
    font-family: "Arimo", Arial, sans-serif;
  }
  .canvas { position: relative; width: 1200px; height: 1023px; }

  .card {
    position: absolute; width: 560px; height: 340px;
    border-radius: 4px; overflow: hidden;
    box-shadow: 0 10px 28px rgba(0,0,0,.22), 0 2px 4px rgba(0,0,0,.12);
  }
  .card-front { left: 70px; top: 90px; background: var(--card-white); }
  .card-back {
    left: 570px; top: 570px;
    background: linear-gradient(160deg, var(--card-grey-top), var(--card-grey-bottom));
  }

  .address-band {
    position: absolute; top: 0; right: 0; bottom: 0; width: 164px;
    background: linear-gradient(135deg, var(--orange-light), var(--orange-deep));
    border-left: 5px solid var(--edge-blue);
  }

  .wordmark {
    position: absolute; display: flex; align-items: center; gap: 10px;
    color: var(--brand-blue); font-weight: 700; white-space: nowrap;
  }
  .wordmark-front { left: 40px; top: 58px; font-size: 24px; }
  .wordmark-mark { width: 20px; height: 20px; background: var(--brand-blue); flex: none; }

  .person { position: absolute; left: 40px; top: 178px; }
  .person-name { color: var(--name-blue); font-size: 21px; font-weight: 700; }
  .person-role { color: var(--ink); font-size: 14px; margin-top: 4px; }

  .contacts { position: absolute; left: 40px; top: 236px; list-style: none; }
  .contacts li {
    display: flex; align-items: center; gap: 7px;
    color: var(--ink); font-size: 13px; line-height: 19px; white-space: nowrap;
  }
  .contacts svg { width: 12px; height: 12px; flex: none; }

  .address {
    position: absolute; left: 414px; top: 148px;
    color: var(--ink); font-size: 13px; line-height: 19px; font-style: normal;
  }
  .address svg { width: 13px; height: 13px; display: block; margin-bottom: 6px; }

  .wordmark-back {
    left: 0; right: 0; top: 138px; justify-content: center;
    font-size: 42px;
  }
  .wordmark-back .wordmark-mark { width: 34px; height: 34px; }
  .back-url {
    position: absolute; left: 34px; bottom: 28px;
    color: var(--ink); font-size: 13px; font-weight: 700;
  }
</style>
</head>
<body>
<main class="canvas">

  <section class="card card-front" aria-label="Business card front">
    <div class="address-band" aria-hidden="true"></div>

    <div class="wordmark wordmark-front">
      <span class="wordmark-mark"></span>
      <span>Riverpeak Analytics</span>
    </div>

    <div class="person">
      <p class="person-name">Marcus Helvard</p>
      <p class="person-role">Managing Director</p>
    </div>

    <ul class="contacts">
      <li>
        <svg viewBox="0 0 12 12" aria-hidden="true"><path d="M1 3 C1 1.5 2.5 1 3.5 1 L4.5 3.5 L3.3 4.5 C4 6 5.5 7.5 7 8.3 L8 7 L11 8 C11 9.5 10 11 8.5 11 C4.5 11 1 7 1 3 Z" fill="var(--name-blue)"/></svg>
        <span>1300 582 417</span>
      </li>
      <li>
        <svg viewBox="0 0 12 12" aria-hidden="true"><rect x="1.5" y="1.5" width="9" height="9" rx="1" fill="none" stroke="var(--ink)" stroke-width="1"/></svg>
        <span>0450 731 258</span>
      </li>
      <li>
        <svg viewBox="0 0 12 12" aria-hidden="true"><rect x="0.5" y="2" width="11" height="8" fill="var(--name-blue)"/><path d="M0.5 2 L6 6.5 L11.5 2" fill="none" stroke="#fff" stroke-width="1"/></svg>
        <span>marcus@riverpeakanalytics.example.au</span>
      </li>
      <li>
        <svg viewBox="0 0 12 12" aria-hidden="true"><circle cx="6" cy="6" r="5.3" fill="none" stroke="var(--name-blue)" stroke-width="1.2"/><ellipse cx="6" cy="6" rx="2.3" ry="5.3" fill="none" stroke="var(--name-blue)" stroke-width="1"/><path d="M0.7 6 H11.3" stroke="var(--name-blue)" stroke-width="1"/></svg>
        <span>www.riverpeakanalytics.example.au</span>
      </li>
    </ul>

    <address class="address">
      <svg viewBox="0 0 13 13" aria-hidden="true"><path d="M6.5 1 L12.5 6.5 H10.5 V12 H7.8 V8.5 H5.2 V12 H2.5 V6.5 H0.5 Z" fill="var(--edge-blue)"/></svg>
      27/15 Marlowe Street<br>Fernbrook NSW 2199
    </address>
  </section>

  <section class="card card-back" aria-label="Business card back">
    <div class="wordmark wordmark-back">
      <span class="wordmark-mark"></span>
      <span>Riverpeak Analytics</span>
    </div>
    <p class="back-url">www.riverpeakanalytics.example.au</p>
  </section>

</main>
</body>
</html>
```